Meadowlark Learning Growth Partners (MLGP)

This is a professional business card. Logo and picture are a must on the front of the card. I am an educational consultant. I have been consulting for the past three years for a company. I am now opening my own company. My goal for my consulting company is to eventually consult all over America.

Target Market(s)

Educators, schools, professionals

Industry/Entity Type

Consulting

Contact Information for Business Card

Picture/logo on front, simple modern design

Font styles to use
Serif

Colors
85abd2
0355a3
3176b5
cedeed

Requirements
Must have
• picture, logo,
• Odessa Pruitt, Ed.S
• address 5073 Cormorant ridge Dr. Nashville, TN 37940
• Cell:616-555-0148
• Office: 629-555-0172
• www.Mlgpedu.example
• pruittodessa@mailbox.example

```html
<!DOCTYPE html>
<html lang="en">
<head>
<meta charset="utf-8">
<title>Meadowlark Learning Growth Partners – Business Card</title>
<link rel="stylesheet" href="https://fonts.googleapis.com/css2?family=Noto+Serif:wght@500;700&display=swap">
<style>
  :root {
    --brand-dark: #0355a3;
    --brand-mid: #3176b5;
    --brand-soft: #85abd2;
    --brand-pale: #cedeed;
    --ink-navy: #0b3f7e;
    --paper: #ffffff;
  }
  * { margin: 0; padding: 0; box-sizing: border-box; }
  html, body { width: 984px; height: 1200px; overflow: hidden; background: var(--paper); }
  body { position: relative; font-family: "Noto Serif", Georgia, serif; }

  .card { position: absolute; left: 0; width: 984px; overflow: hidden; background: var(--brand-pale); }
  .card--front { top: 0; height: 562px; }
  .card--back { top: 637px; height: 563px; }
  .card-shapes { position: absolute; inset: 0; }

  .holder-name {
    position: absolute; right: 24px; top: 30px;
    font-size: 41px; font-weight: 700; color: var(--paper); letter-spacing: 0.5px;
  }

  .lockup { position: absolute; display: flex; align-items: center; color: var(--ink-navy); font-weight: 700; }
  .lockup-dot { border-radius: 50%; background: var(--ink-navy); flex: none; }
  .lockup-short { letter-spacing: 3px; }
  .lockup-rule { background: var(--ink-navy); flex: none; }
  .lockup-full { line-height: 1.3; }

  .card--front .lockup { left: 34px; top: 152px; }
  .card--front .lockup-dot { width: 40px; height: 40px; margin-right: 20px; }
  .card--front .lockup-short { font-size: 50px; margin-right: 28px; }
  .card--front .lockup-rule { width: 2px; height: 148px; margin-right: 24px; }
  .card--front .lockup-full { font-size: 29px; }

  .card--back .lockup { left: 34px; top: 808px; top: 170px; }
  .card--back .lockup-dot { width: 62px; height: 62px; margin-right: 24px; }
  .card--back .lockup-short { font-size: 74px; margin-right: 38px; }
  .card--back .lockup-rule { width: 3px; height: 212px; margin-right: 32px; }
  .card--back .lockup-full { font-size: 45px; }

  .portrait {
    position: absolute; left: 767px; top: 161px; width: 168px; height: 220px;
    background: linear-gradient(180deg, #d9c7a8 0%, #b79c83 40%, #1d1f26 72%, #15171c 100%);
  }

  .contact-list { position: absolute; left: 26px; top: 398px; list-style: none; color: var(--paper); }
  .contact-list li { display: flex; align-items: center; height: 36.5px; font-size: 22px; font-weight: 500; }
  .contact-icon { width: 20px; height: 20px; margin-right: 10px; flex: none; }

  .address { position: absolute; left: 630px; top: 470px; color: var(--paper); font-size: 22px; font-weight: 500; line-height: 39px; }
  .address-line { display: flex; align-items: center; }
  .address-line--second { padding-left: 17px; }
  .pin-icon { width: 12px; height: 18px; margin-right: 5px; }
</style>
</head>
<body>

<section class="card card--front">
  <svg class="card-shapes" width="984" height="562" viewBox="0 0 984 562" aria-hidden="true">
    <polygon points="0,0 984,0 984,161 0,64" fill="var(--brand-dark)"/>
    <path d="M0,317 L431,361 C500,370 560,440 581,562 L0,562 Z" fill="var(--brand-dark)"/>
    <path d="M548,466 C590,410 640,388 700,392 L984,436 L984,562 L581,562 C574,520 563,490 548,466 Z" fill="var(--brand-mid)"/>
  </svg>

  <h1 class="holder-name">Odessa Pruitt, Ed.S</h1>

  <div class="lockup">
    <span class="lockup-dot"></span>
    <span class="lockup-short">MLGP</span>
    <span class="lockup-rule"></span>
    <span class="lockup-full">Meadowlark<br>Learning<br>Growth<br>Partners</span>
  </div>

  <div class="portrait" role="img" aria-label="Portrait photo of Odessa Pruitt"></div>

  <ul class="contact-list">
    <li>
      <svg class="contact-icon" viewBox="0 0 20 20" aria-hidden="true"><rect x="1" y="1" width="18" height="18" rx="3" fill="#fff"/><path d="M7 4.5c-1 .5-1.8 1.6-1.5 3.2.6 3 3.6 6.4 6.4 7.5 1.5.5 2.6-.3 3.1-1.2l-2-1.7-1.2.9c-1.3-.6-2.8-2.3-3.3-3.7l1-1.1Z" fill="var(--brand-dark)"/></svg>
      616-555-0148
    </li>
    <li>
      <svg class="contact-icon" viewBox="0 0 20 20" aria-hidden="true"><path d="M1 7c0-3 18-3 18 0v2h-4V7.5H5V9H1Z" fill="#fff"/><rect x="3" y="9" width="14" height="10" rx="1.5" fill="#fff"/><circle cx="10" cy="14" r="2.6" fill="var(--brand-dark)"/></svg>
      629-555-0172
    </li>
    <li>
      <svg class="contact-icon" viewBox="0 0 20 20" aria-hidden="true"><rect x="0" y="2" width="20" height="16" fill="#fff"/><circle cx="9" cy="10" r="5" fill="none" stroke="var(--brand-dark)" stroke-width="1.3"/><path d="M4 10h10M9 5v10" stroke="var(--brand-dark)" stroke-width="1"/></svg>
      www.Mlgpedu.example
    </li>
    <li>
      <svg class="contact-icon" viewBox="0 0 20 20" aria-hidden="true"><rect x="1" y="3" width="18" height="14" fill="none" stroke="#fff" stroke-width="1.6"/><path d="M1 3l9 8 9-8M1 17l7-6M19 17l-7-6" fill="none" stroke="#fff" stroke-width="1.3"/></svg>
      pruittodessa@mailbox.example
    </li>
  </ul>

  <address class="address" style="font-style:normal">
    <span class="address-line"><svg class="pin-icon" viewBox="0 0 12 18" aria-hidden="true"><path d="M6 1a5 5 0 0 0-5 5c0 4 5 11 5 11s5-7 5-11a5 5 0 0 0-5-5Z" fill="none" stroke="#fff" stroke-width="1.6"/><circle cx="6" cy="6" r="1.7" fill="#fff"/></svg>5073 Cormorant ridge</span>
    <span class="address-line address-line--second">Dr. Nashville, TN 37940</span>
  </address>
</section>

<section class="card card--back">
  <svg class="card-shapes" width="984" height="563" viewBox="0 0 984 563" aria-hidden="true">
    <polygon points="0,0 984,0 984,103 0,38" fill="var(--brand-dark)"/>
    <polygon points="0,464 984,530 984,563 0,563" fill="var(--brand-mid)"/>
  </svg>

  <div class="lockup">
    <span class="lockup-dot"></span>
    <span class="lockup-short">MLGP</span>
    <span class="lockup-rule"></span>
    <span class="lockup-full">Meadowlark<br>Learning<br>Growth<br>Partners</span>
  </div>
</section>

</body>
</html>
```